ARC VOLLEY Business Card Project

I'd like to request a business card design for the new company I've launched.
The name of the company is "ARC VOLLEY" an indoor unmanned tennis practice facility.
We would like to see designs that use our brand identity color in the logo I've attached.
We hope to get the design with modern, luxurious and elegant tone and manner.
We hope the logo should not be too big.

Business card must have elements as below:
- Logo (One of the logos I've attached)
- Name (In Korean Text) : 박 서 윤
- Title (In Korean Text) : 대표
- Phone Number : 010-8472-3916
- Email Address : seoyun.park@arcvolley-example.co.kr
- Website : www.arcvolley-example.co.kr
- Instagram : arcvolley
- Address (In Korean text) : 경기도 용인시 수지구 풍덕천로 456 미래타워 5층 501호, 502호

Target Market(s)

Tennis amateurs in 20 to 40s

Industry/Entity Type

Sports, Hobby

Contact Information for Business Card

- Logo (One of the logos I've attached) - Name (In Korean Text) : 박 서 윤 - Title (In Korean Text) : 대표 - Phone Number : 010-8472-3916 - Email Address : seoyun.park@arcvolley-example.co.kr - Website : www.arcvolley-example.co.kr - Instagram : arcvolley - Address (In Korean text) : 경기도 용인시 수지구 풍덕천로 456 미래타워 5층 501호, 502호

Font styles to use
Sans Serif

Requirements
Must have
• Double sided
Nice to have
• Logo with intaglio or relief embossing
Should not have
• Logo should not be too big.

```html
<!DOCTYPE html>
<html lang="ko">
<head>
<meta charset="utf-8">
<title>ARC VOLLEY Business Card</title>
<link rel="stylesheet" href="https://fonts.googleapis.com/css2?family=Noto+Sans+KR:wght@400;500&family=Open+Sans:wght@400;600&display=swap">
<style>
  :root {
    --backdrop: #1c3a2d;
    --card-white: #f7f7f5;
    --brand-green: #2f5a3e;
    --card-dark: #2a4a35;
    --card-dark-deep: #1f3a29;
    --edge-green: #1fa134;
    --on-dark: #ffffff;
  }
  * { margin: 0; padding: 0; box-sizing: border-box; }
  html, body {
    width: 1200px; height: 1200px; overflow: hidden;
    background: var(--backdrop);
  }
  .canvas {
    position: relative; width: 1200px; height: 1200px;
  }
  .card {
    position: absolute; left: 160px; width: 880px; height: 503px;
    border-bottom: 4px solid var(--edge-green);
    box-shadow: 0 14px 30px rgba(0,0,0,0.35);
  }
  .card-front { top: 64px; background: var(--card-white); color: var(--brand-green); }
  .card-back { top: 633px; overflow: hidden; }

  .brand-lockup {
    position: absolute; display: flex; align-items: center; gap: 14px;
    font-family: "Open Sans", sans-serif; font-weight: 600; letter-spacing: 0.06em;
  }
  .card-front .brand-lockup { top: 92px; right: 90px; font-size: 40px; color: var(--brand-green); }
  .brand-dot { border-radius: 50%; border: 4px solid currentColor; }
  .card-front .brand-dot { width: 52px; height: 52px; }

  .person { position: absolute; left: 72px; top: 140px; font-family: "Noto Sans KR", sans-serif; font-weight: 400; }
  .person-name { font-size: 44px; line-height: 1.15; letter-spacing: 0.04em; }
  .person-title { font-size: 38px; line-height: 1.2; }

  .contact-list {
    position: absolute; left: 72px; top: 298px; list-style: none;
    font-family: "Open Sans", sans-serif; font-size: 25px; line-height: 33px;
  }
  .contact-item { display: flex; align-items: center; gap: 14px; }
  .contact-icon { width: 20px; height: 20px; flex: none; fill: var(--brand-green); }
  .contact-address { font-family: "Noto Sans KR", sans-serif; font-size: 21px; }

  .back-photo {
    position: absolute; inset: 0;
    background: linear-gradient(120deg, var(--card-dark) 0%, #35573f 45%, var(--card-dark-deep) 100%);
  }
  .card-back .brand-lockup {
    left: 50%; top: 50%; transform: translate(-50%, -50%);
    font-size: 56px; color: var(--on-dark); flex-direction: column; gap: 18px;
  }
  .card-back .brand-dot { width: 96px; height: 96px; border-width: 5px; }
</style>
</head>
<body>
<main class="canvas">
  <section class="card card-front" aria-label="Business card front">
    <div class="brand-lockup"><span class="brand-dot"></span><span class="brand-name">ARC VOLLEY</span></div>
    <div class="person">
      <p class="person-name">박 서 윤</p>
      <p class="person-title">대표</p>
    </div>
    <ul class="contact-list">
      <li class="contact-item">
        <svg class="contact-icon" viewBox="0 0 24 24"><path d="M6.6 10.8a15 15 0 0 0 6.6 6.6l2.2-2.2a1 1 0 0 1 1-.25 11.4 11.4 0 0 0 3.6.57 1 1 0 0 1 1 1V20a1 1 0 0 1-1 1A17 17 0 0 1 3 4a1 1 0 0 1 1-1h3.5a1 1 0 0 1 1 1c0 1.25.2 2.45.57 3.57a1 1 0 0 1-.25 1z"/></svg>
        <span>010-8472-3916</span>
      </li>
      <li class="contact-item">
        <svg class="contact-icon" viewBox="0 0 24 24"><path d="M2 5h20v14H2z M3 6l9 7 9-7" fill="none" stroke="#2f5a3e" stroke-width="2"/></svg>
        <span>seoyun.park@arcvolley-example.co.kr</span>
      </li>
      <li class="contact-item">
        <svg class="contact-icon" viewBox="0 0 24 24"><g fill="none" stroke="#2f5a3e" stroke-width="1.8"><circle cx="12" cy="12" r="9"/><ellipse cx="12" cy="12" rx="4" ry="9"/><path d="M3 12h18M5 7h14M5 17h14"/></g></svg>
        <span>www.arcvolley-example.co.kr</span>
      </li>
      <li class="contact-item">
        <svg class="contact-icon" viewBox="0 0 24 24"><circle cx="12" cy="12" r="8" fill="none" stroke="#2f5a3e" stroke-width="2.2"/></svg>
        <span>@arcvolley</span>
      </li>
      <li class="contact-item contact-address">
        <svg class="contact-icon" viewBox="0 0 24 24"><path d="M12 2a7 7 0 0 0-7 7c0 5 7 13 7 13s7-8 7-13a7 7 0 0 0-7-7zm0 9.5A2.5 2.5 0 1 1 12 6.5a2.5 2.5 0 0 1 0 5z"/></svg>
        <span>경기도 용인시 수지구 풍덕천로 456 미래타워 5층 501호, 502호</span>
      </li>
    </ul>
  </section>

  <section class="card card-back" aria-label="Business card back">
    <div class="back-photo" role="img" aria-label="Green-toned photo of a tennis player swinging a racket on an outdoor court"></div>
    <div class="brand-lockup"><span class="brand-dot"></span><span class="brand-name">ARC VOLLEY</span></div>
  </section>
</main>
</body>
</html>
```